hair salon logo and Business Card Design

this logo needs to reflect a vibrant, trendy and fun business, targeting 20 to 50 year old ladies in a nice sunny part of Australia.Our aim is to make everyone feel in a fantastic mood when they walk out of the salon,and look equally glamorous.
I would like the logo to be simple yet using bold colors and font.
ideally the name mirra would be lowercase with a nice rounded shape and hair+beauty, with upper case and the letter i in an inverted position.

Industry/Entity Type

Hair

Contact Information for Business Card

mirra
hair | beauty.

Lia Forsett
stylist/owner
0419376052
58 Wexcombe St. Scarborough QLD. 4020

Requirements
Must have
• front all the business details
back lined for writing notes.
Nice to have
• use of bold stand out colors, simple shapes sense of movement, not stillness, modern, professional.

```html
<!DOCTYPE html>
<html lang="en">
<head>
<meta charset="utf-8">
<title>mirra Hair | Beauty – business card</title>
<link href="https://fonts.googleapis.com/css2?family=Questrial&family=Didact+Gothic&display=swap" rel="stylesheet">
<style>
  :root {
    --magenta: #c0146e;
    --magenta-deep: #7c0843;
    --magenta-light: #e2499a;
    --black: #0d0d0f;
    --charcoal: #2a2a2e;
    --white: #ffffff;
    --page: #ece9e6;
  }
  * { box-sizing: border-box; margin: 0; padding: 0; }
  html, body { width: 1200px; height: 1001px; overflow: hidden; }
  body {
    background: var(--page);
    font-family: "Questrial", "Didact Gothic", sans-serif;
    color: var(--white);
    position: relative;
  }
  .card {
    position: absolute;
    left: 220px;
    width: 760px;
    height: 434px;
    border-radius: 28px;
    overflow: hidden;
    box-shadow: 0 6px 18px rgba(0,0,0,.18);
  }
  .card--front { top: 44px; }
  .card--back { top: 523px; }
  .card__bg { position: absolute; inset: 0; width: 100%; height: 100%; display: block; }

  /* front */
  .logo-figure {
    position: absolute;
    left: 320px; top: 24px;
    width: 120px; height: 140px;
    border-radius: 50% 50% 18px 18px;
    background: radial-gradient(circle at 50% 35%, rgba(255,255,255,.85), rgba(255,255,255,.35) 60%, rgba(255,255,255,0) 72%);
  }
  .logo-name {
    position: absolute;
    left: 0; right: 0; top: 160px;
    text-align: center;
    font-size: 46px;
    letter-spacing: 1px;
  }
  .slogan {
    position: absolute;
    left: 0; right: 0; top: 348px;
    text-align: center;
    font-size: 21px;
    letter-spacing: .5px;
  }

  /* back */
  .stylist-figure {
    position: absolute;
    left: 58px; top: 70px;
    width: 150px; height: 190px;
    border-radius: 50% 50% 22px 22px;
    background: radial-gradient(circle at 50% 38%, var(--magenta-light), var(--magenta) 55%, rgba(192,20,110,0) 74%);
  }
  .business {
    position: absolute;
    right: 48px; top: 60px;
    text-align: right;
  }
  .business__name { font-size: 31px; letter-spacing: .5px; }
  .business__address { font-size: 17px; line-height: 1.3; margin-top: 10px; }
  .contact {
    position: absolute;
    left: 440px; top: 184px;
    list-style: none;
    font-size: 18px;
  }
  .contact__item { display: flex; align-items: center; gap: 10px; margin-bottom: 10px; }
  .contact__icon { width: 24px; height: 24px; flex: none; }
  .person {
    position: absolute;
    left: 62px; top: 352px;
  }
  .person__name { font-size: 29px; font-weight: 700; font-family: "Didact Gothic", sans-serif; }
  .person__role { font-size: 21px; margin-top: 2px; }
</style>
</head>
<body>

<section class="card card--front" aria-label="Card front">
  <svg class="card__bg" viewBox="0 0 760 434" preserveAspectRatio="none" aria-hidden="true">
    <defs>
      <radialGradient id="frontGlow" cx="50%" cy="30%" r="75%">
        <stop offset="0" stop-color="#e2499a"/>
        <stop offset=".45" stop-color="#c0146e"/>
        <stop offset="1" stop-color="#7c0843"/>
      </radialGradient>
      <linearGradient id="frontBand" x1="0" y1="0" x2="0" y2="1">
        <stop offset="0" stop-color="#2a2a2e"/>
        <stop offset="1" stop-color="#0d0d0f"/>
      </linearGradient>
    </defs>
    <rect width="760" height="434" fill="url(#frontGlow)"/>
    <path d="M0 300 Q420 282 760 212" fill="none" stroke="#0d0d0f" stroke-width="3" opacity=".6"/>
    <path d="M0 312 Q420 296 760 226 L760 434 L0 434 Z" fill="url(#frontBand)"/>
  </svg>
  <div class="logo-figure" role="img" aria-label="Salon emblem: illustrated woman with ornate swirling hair"></div>
  <div class="logo-name">mirra</div>
  <p class="slogan">your slogan here</p>
</section>

<section class="card card--back" aria-label="Card back">
  <svg class="card__bg" viewBox="0 0 760 434" preserveAspectRatio="none" aria-hidden="true">
    <defs>
      <linearGradient id="backDark" x1="0" y1="0" x2="1" y2="1">
        <stop offset="0" stop-color="#0d0d0f"/>
        <stop offset=".6" stop-color="#2a2a2e"/>
        <stop offset="1" stop-color="#0d0d0f"/>
      </linearGradient>
      <linearGradient id="backBand" x1="0" y1="0" x2="1" y2="0">
        <stop offset="0" stop-color="#c0146e"/>
        <stop offset=".5" stop-color="#e2499a"/>
        <stop offset="1" stop-color="#c0146e"/>
      </linearGradient>
    </defs>
    <rect width="760" height="434" fill="url(#backDark)"/>
    <path d="M0 318 Q400 302 760 282" fill="none" stroke="#c0146e" stroke-width="4"/>
    <path d="M0 338 Q400 322 760 300 L760 434 L0 434 Z" fill="url(#backBand)"/>
  </svg>

  <div class="stylist-figure" role="img" aria-label="Illustrated woman with ornate swirling hair in magenta"></div>

  <div class="business">
    <p class="business__name">mirra&nbsp; Hair | Beauty.</p>
    <p class="business__address">58 Wexcombe<br>St. Larkhaven QLD. 4127</p>
  </div>

  <ul class="contact">
    <li class="contact__item">
      <svg class="contact__icon" viewBox="0 0 24 24" aria-hidden="true">
        <circle cx="12" cy="12" r="12" fill="#ffffff"/>
        <path d="M8.5 6.5l2 2.2-1.2 1.6c.8 1.7 2 2.9 3.6 3.7l1.6-1.2 2.2 2-1.3 1.8c-4.2-.6-7.8-4.2-8.4-8.4z" fill="#0d0d0f"/>
      </svg>
      <span>0419376052</span>
    </li>
    <li class="contact__item">
      <svg class="contact__icon" viewBox="0 0 24 24" aria-hidden="true">
        <circle cx="12" cy="12" r="12" fill="#ffffff"/>
        <rect x="6" y="8" width="12" height="8.5" rx="1" fill="#0d0d0f"/>
        <path d="M6.5 8.6l5.5 4.2 5.5-4.2" fill="none" stroke="#ffffff" stroke-width="1.2"/>
      </svg>
      <span>hello@mirrasalon.com</span>
    </li>
  </ul>

  <div class="person">
    <p class="person__name">Lia Forsett</p>
    <p class="person__role">stylist/owner</p>
  </div>
</section>

</body>
</html>
```